Varlow Business Partners
Business Cards & Stationery
Professional
Thomas E. Varlow
CEO
58 Birch Lane, North
Suite 318
Edgeton, NJ 07415
thomas.varlow@varlowbp.com
Back of card should contain the black version of the logo - no other information

```html
<!DOCTYPE html>
<html lang="en">
<head>
<meta charset="utf-8">
<title>Varlow Business Partners — Stationery</title>
<link href="https://fonts.googleapis.com/css2?family=Open+Sans:wght@400;600;700&display=swap" rel="stylesheet">
<style>
  :root {
    --board: #2a2a2a;
    --paper: #ffffff;
    --paper-shade: #f1f1f1;
    --orange: #f26a1b;
    --ink: #222222;
    --muted: #8a8a8a;
    --label: #bdbdbd;
    --black: #111111;
    --watermark: #f6d9c6;
  }
  * { margin: 0; padding: 0; box-sizing: border-box; }
  html, body { width: 1200px; height: 413px; overflow: hidden; }
  body {
    background: var(--board);
    font-family: "Open Sans", Arial, sans-serif;
    position: relative;
    color: var(--ink);
  }
  .piece { position: absolute; background: var(--paper); overflow: hidden; box-shadow: 0 2px 6px rgba(0,0,0,.45); }
  .label { position: absolute; font-size: 5px; color: var(--label); text-align: center; }
  .mark { font-weight: 700; color: var(--ink); letter-spacing: .5px; line-height: 1; position: absolute; }
  .mark.orange { color: var(--orange); }
  .mark.white { color: var(--paper); }
  .tagline { position: absolute; font-size: 3px; line-height: 1.3; color: var(--muted); font-weight: 600; text-transform: uppercase; }
  .watermark { position: absolute; font-weight: 700; color: var(--watermark); line-height: 1; }

  /* Business cards */
  .card { width: 84px; height: 50px; }
  .card-front { left: 46px; top: 104px; }
  .card-front .details { position: absolute; left: 0; top: 0; width: 46px; height: 100%; background: var(--paper); padding: 8px 4px; }
  .card-front .band { position: absolute; right: 0; top: 0; width: 38px; height: 100%; background: var(--orange); }
  .card-front .name { font-size: 4px; font-weight: 700; }
  .card-front .role { font-size: 3px; color: var(--orange); margin-bottom: 3px; }
  .card-front .line { font-size: 2.4px; color: var(--muted); line-height: 1.4; }
  .card-front .mark { right: 8px; top: 18px; font-size: 9px; }
  .card-back-light { left: 46px; top: 241px; }
  .card-back-light .mark { left: 14px; top: 16px; font-size: 16px; }
  .card-back-light .tagline { left: 48px; top: 20px; }
  .card-back-dark { left: 46px; top: 352px; background: var(--black); }
  .card-back-dark .mark { left: 14px; top: 16px; font-size: 16px; }
  .card-back-dark .tagline { left: 48px; top: 20px; color: var(--label); }

  /* Letterheads */
  .letterhead { width: 207px; height: 360px; top: 18px; background: var(--paper-shade); }
  .letterhead-one { left: 181px; }
  .letterhead-two { left: 413px; }
  .letterhead .mark { left: 26px; top: 22px; font-size: 16px; }
  .letterhead .tagline { left: 62px; top: 25px; }
  .letterhead .contact { position: absolute; left: 112px; top: 22px; font-size: 2.6px; color: var(--muted); line-height: 1.5; border-left: 1px solid var(--orange); padding-left: 3px; }
  .letterhead .watermark { left: 30px; top: 110px; font-size: 78px; }
  .letterhead .footer-bar { position: absolute; left: 0; bottom: 0; width: 100%; height: 7px; background: var(--orange); }
  .letterhead-two .footer-bar { height: 14px; }
  .letterhead-two .footer-text { position: absolute; left: 0; bottom: 5px; width: 100%; text-align: center; font-size: 2.6px; color: var(--paper); }

  /* Envelopes */
  .envelope { width: 198px; height: 80px; }
  .envelope svg.flap { position: absolute; left: 0; top: 0; width: 100%; height: 34px; }
  .env-orange { left: 805px; top: 14px; }
  .env-orange .mark { left: 96px; top: 10px; font-size: 10px; }
  .env-black { left: 880px; top: 92px; background: var(--black); z-index: 2; }
  .env-black .mark { left: 94px; top: 10px; font-size: 10px; }
  .env-white { left: 880px; top: 176px; z-index: 3; }
  .env-white .mark { left: 94px; top: 10px; font-size: 10px; }
  .env-front { left: 808px; top: 246px; width: 196px; height: 132px; z-index: 4; }
  .env-front .mark { left: 10px; top: 10px; font-size: 10px; }
  .env-front .line { position: absolute; left: 10px; font-size: 2.4px; color: var(--muted); }
  .env-front .watermark { left: 110px; top: 48px; font-size: 54px; }
  .env-front .footer-bar { position: absolute; left: 0; bottom: 0; width: 100%; height: 5px; background: var(--orange); }
</style>
</head>
<body>

  <!-- Business cards -->
  <div class="piece card card-front">
    <div class="details">
      <div class="name">Thomas E. Varlow</div>
      <div class="role">CEO</div>
      <div class="line">58 Birch Lane, North</div>
      <div class="line">Suite 318</div>
      <div class="line">Edgeton, NJ 07415</div>
      <div class="line">thomas.varlow@varlowbp.com</div>
    </div>
    <div class="band"><span class="mark white">VBP</span></div>
  </div>
  <div class="label" style="left:46px;top:158px;width:84px;">Business Card Front</div>

  <div class="piece card card-back-light">
    <span class="mark">VBP</span>
    <span class="tagline">Varlow<br>Business<br>Partners</span>
  </div>
  <div class="label" style="left:46px;top:295px;width:84px;">Back Light Option</div>

  <div class="piece card card-back-dark">
    <span class="mark white">VBP</span>
    <span class="tagline">Varlow<br>Business<br>Partners</span>
  </div>
  <div class="label" style="left:46px;top:404px;width:84px;">Back Dark Option</div>

  <!-- Letterheads -->
  <div class="piece letterhead letterhead-one">
    <span class="mark">VBP</span>
    <span class="tagline">Varlow<br>Business<br>Partners</span>
    <div class="contact">58 Birch Lane, North<br>Suite 318<br>Edgeton, NJ 07415<br>thomas.varlow@varlowbp.com</div>
    <span class="watermark">VBP</span>
    <div class="footer-bar"></div>
  </div>
  <div class="label" style="left:181px;top:382px;width:207px;">Letterhead Option One</div>

  <div class="piece letterhead letterhead-two">
    <span class="mark">VBP</span>
    <span class="tagline">Varlow<br>Business<br>Partners</span>
    <span class="watermark">VBP</span>
    <div class="footer-bar"></div>
    <div class="footer-text">58 Birch Lane, North &nbsp;·&nbsp; Suite 318 &nbsp;·&nbsp; Edgeton, NJ 07415 &nbsp;·&nbsp; thomas.varlow@varlowbp.com</div>
  </div>
  <div class="label" style="left:413px;top:382px;width:207px;">Letterhead Option Two</div>

  <!-- Envelopes -->
  <div class="piece envelope env-orange">
    <svg class="flap" viewBox="0 0 198 34" preserveAspectRatio="none"><polygon points="0,0 198,0 99,34" fill="#f26a1b"/></svg>
    <span class="mark white">VBP</span>
  </div>
  <div class="piece envelope env-black">
    <svg class="flap" viewBox="0 0 198 34" preserveAspectRatio="none"><polygon points="0,0 198,0 99,34" fill="#ffffff"/></svg>
    <span class="mark">VBP</span>
  </div>
  <div class="piece envelope env-white">
    <svg class="flap" viewBox="0 0 198 34" preserveAspectRatio="none"><polygon points="0,0 198,0 99,34" fill="#ffffff" stroke="#dddddd" stroke-width="1"/></svg>
    <span class="mark orange">VBP</span>
  </div>
  <div class="piece envelope env-front">
    <span class="mark">VBP</span>
    <div class="line" style="top:24px;">58 Birch Lane, North</div>
    <div class="line" style="top:28px;">Suite 318</div>
    <div class="line" style="top:32px;">Edgeton, NJ 07415</div>
    <span class="watermark">VBP</span>
    <div class="footer-bar"></div>
  </div>
  <div class="label" style="left:808px;top:382px;width:196px;">Envelope Options</div>

</body>
</html>
```